Business Card Design for a Personal Trainer

I need a business card design for my job as a personal trainer. It should have a unique, modern and exclusive design. On the front there should be only my logo with my name and my job. 0163/2918374 Tobias Kellinger Lindenfeldweg 14 80412 Munich Germany The most important contact information is the web adress. it can be bigger than the rest, but its not necessary. The card should be 8,5cmx5,5cm big. Font: Roboto. Colors: black, white, gray, 56c1ff.

```html
<!DOCTYPE html>
<html lang="de">
<head>
<meta charset="utf-8">
<title>Tobias Kellinger – Personal Trainer Business Card</title>
<link href="https://fonts.googleapis.com/css2?family=Roboto:wght@300;400;700&display=swap" rel="stylesheet">
<style>
  :root {
    --page-bg: #4a4a4a;
    --card-dark: #262626;
    --white: #ffffff;
    --text-light: #e6e6e6;
    --accent: #56c1ff;
    --front-top: #3b3a4a;
    --front-mid: #5c5a72;
    --front-low: #2a2935;
    --portrait-a: #5a5a5a;
    --portrait-b: #2f2f2f;
  }
  * { box-sizing: border-box; margin: 0; padding: 0; }
  html, body {
    width: 1200px; height: 1021px; overflow: hidden;
    background: var(--page-bg);
    font-family: "Roboto", sans-serif;
  }
  .sheet {
    position: relative; width: 1200px; height: 1021px;
    display: flex; flex-direction: column; align-items: center; justify-content: center; gap: 34px;
  }
  .card {
    position: relative; width: 720px; height: 466px; overflow: hidden;
    box-shadow: 0 14px 30px rgba(0,0,0,0.45);
  }
  /* Front */
  .card-front .scene-photo {
    position: absolute; inset: 0;
    background:
      radial-gradient(ellipse at 72% 30%, var(--front-mid) 0%, transparent 55%),
      linear-gradient(180deg, var(--front-top) 0%, #4a4860 45%, var(--front-low) 100%);
  }
  .front-brand {
    position: absolute; left: 0; right: 0; top: 150px;
    display: flex; flex-direction: column; align-items: center; color: var(--white);
  }
  .brand-square {
    width: 44px; height: 44px; background: var(--white); margin-bottom: 26px;
  }
  .brand-name {
    font-weight: 400; font-size: 44px; letter-spacing: 3px; text-transform: uppercase; line-height: 1;
  }
  .brand-role {
    display: flex; align-items: center; gap: 14px; margin-top: 8px; width: 470px;
  }
  .brand-role .rule { flex: 1; height: 2px; background: var(--white); }
  .brand-role span {
    font-size: 17px; font-weight: 300; letter-spacing: 7px; text-transform: uppercase;
  }
  /* Back */
  .card-back { background: var(--card-dark); }
  .card-back .portrait-photo {
    position: absolute; left: 40px; top: 40px; width: 300px; height: 426px;
    background: radial-gradient(ellipse at 50% 45%, var(--portrait-a) 0%, var(--portrait-b) 65%, transparent 80%);
  }
  .contact {
    position: absolute; left: 340px; right: 20px; top: 110px;
    display: flex; flex-direction: column; align-items: center; text-align: center; color: var(--text-light);
  }
  .contact-brand {
    color: var(--white); font-size: 30px; font-weight: 400; margin-bottom: 26px;
    display: flex; align-items: center; gap: 12px;
  }
  .contact-brand i { display: block; width: 22px; height: 22px; background: var(--white); }
  .web { color: var(--accent); font-weight: 700; font-size: 27px; margin-bottom: 22px; }
  .line { font-size: 20px; font-weight: 400; line-height: 1.3; }
  .divider { width: 70px; height: 2px; background: var(--accent); margin: 18px 0; }
</style>
</head>
<body>
<main class="sheet">
  <section class="card card-front">
    <div class="scene-photo" role="img" aria-label="Moody twilight beach scene with a runner standing at the water's edge"></div>
    <div class="front-brand">
      <div class="brand-square"></div>
      <div class="brand-name">Tobias Kellinger</div>
      <div class="brand-role"><div class="rule"></div><span>Personal Trainer</span><div class="rule"></div></div>
    </div>
  </section>

  <section class="card card-back">
    <div class="portrait-photo" role="img" aria-label="Black and white portrait of the trainer with arms crossed"></div>
    <div class="contact">
      <div class="contact-brand"><i></i>Tobias Kellinger</div>
      <div class="web">www.tobiaskellinger.de</div>
      <div class="line">0163/2918374</div>
      <div class="line">t.kellinger@postfach.de</div>
      <div class="divider"></div>
      <div class="line">Lindenfeldweg 14</div>
      <div class="line">80412 München</div>
    </div>
  </section>
</main>
</body>
</html>
```